Brindle's Coating & Renewal Letterhead Design We want to revamp out old traditional letterhead with the new logo designs that are attached. We are working on getting all our company items from vehicles, business, cards, t-shirts, letterhead to match. This should include company colors, fonts, and flow of items that we have attached below.

Industry/Entity Type

Construction Company

Font styles to use
Sans Serif
Other font styles liked:
• Bold with outline

Colors
ec1f27
ffffff

Requirements
Must have
• Company Name: Brindle's Coating & Renewal
• Address: 4172 SW 83rd Ter Harrow Cove fl 30418
• Office Number: (555) 240-6193
• Email: brindlesrenewal@mailnest-example.com
• License Number: QRT8046392
Nice to have
• Company Colors: red, white, black, and grey

```html
<!DOCTYPE html>
<html lang="en">
<head>
<meta charset="utf-8">
<title>Brindle's Coating &amp; Renewal — Letterhead</title>
<link href="https://fonts.googleapis.com/css2?family=Lato:wght@300;400;900&display=swap" rel="stylesheet">
<style>
  :root {
    --brand-red: #ec1f27;
    --ink: #1d1d1d;
    --rule-grey: #a9a6a4;
    --paper: #fdfcf9;
    --backdrop: #cfc3c0;
    --watermark-red: rgba(236, 31, 39, 0.05);
    --watermark-grey: rgba(60, 60, 60, 0.05);
  }
  * { box-sizing: border-box; margin: 0; padding: 0; }
  html, body {
    width: 1200px; height: 784px; overflow: hidden;
    background: var(--backdrop);
    font-family: "Lato", "Helvetica Neue", Arial, sans-serif;
  }
  .letterhead {
    position: absolute; left: 320px; top: 30px;
    width: 560px; height: 724px;
    background: var(--paper);
    box-shadow: 0 6px 18px rgba(0,0,0,0.18);
    overflow: hidden;
  }
  .edge-band {
    position: absolute; left: 0; top: 0; bottom: 0; width: 9px;
    background: var(--brand-red);
  }
  .edge-rule {
    position: absolute; left: 24px; top: 0; bottom: 0; width: 1px;
    background: var(--rule-grey);
  }
  .license {
    position: absolute; left: 18px; top: 400px;
    width: 14px; height: 170px;
    background: var(--paper);
    display: flex; align-items: center; justify-content: center;
  }
  .license span {
    display: block; transform: rotate(-90deg);
    font-size: 10.5px; letter-spacing: 0.2px;
    color: var(--brand-red); white-space: nowrap;
  }
  .company-name {
    position: absolute; right: 36px; top: 34px;
    text-align: right; color: var(--brand-red);
    font-weight: 900; text-transform: uppercase; line-height: 1.02;
  }
  .company-name .primary { display: block; font-size: 38px; letter-spacing: 1px; }
  .company-name .secondary { display: block; font-size: 17px; letter-spacing: 1.5px; }
  .contact {
    position: absolute; right: 36px; top: 190px;
    text-align: right; font-size: 10.5px; line-height: 1.45; color: var(--ink);
    list-style: none;
  }
  .contact .address { color: var(--brand-red); }
  .contact li { display: flex; justify-content: flex-end; align-items: center; gap: 5px; }
  .contact svg { width: 9px; height: 9px; flex: none; }
  .anniversary-mark {
    position: absolute; left: 140px; top: 300px;
    width: 270px; height: 250px;
  }
</style>
</head>
<body>
  <main class="letterhead">
    <div class="edge-band"></div>
    <div class="edge-rule"></div>
    <p class="license"><span>LICENSE NUMBER: QRT8046392</span></p>

    <h1 class="company-name">
      <span class="primary">Brindle's</span>
      <span class="secondary">Coating &amp; Renewal</span>
    </h1>

    <ul class="contact">
      <li class="address">4172 SW 83rd Ter</li>
      <li class="address">Harrow Cove fl 30418</li>
      <li>
        <svg viewBox="0 0 10 10"><path d="M2 1 L4 1 L4.6 3 L3.4 4 Q4.4 5.8 6 6.6 L7 5.4 L9 6 L9 8 Q9 9 8 9 Q1 8.4 1 2 Q1 1 2 1Z" fill="var(--brand-red)"/></svg>
        (555) 240-6193
      </li>
      <li>
        <svg viewBox="0 0 10 10"><rect x="0.5" y="2" width="9" height="6.5" fill="var(--brand-red)"/><path d="M0.5 2 L5 5.8 L9.5 2" stroke="#fff" stroke-width="0.9" fill="none"/></svg>
        brindlesrenewal@mailnest-example.com
      </li>
      <li>
        <svg viewBox="0 0 10 10"><circle cx="5" cy="5" r="4.3" fill="none" stroke="var(--brand-red)" stroke-width="1"/><path d="M0.7 5 H9.3 M5 0.7 V9.3" stroke="var(--brand-red)" stroke-width="0.8"/></svg>
        www.brindlesrenewal-example.com
      </li>
    </ul>

    <svg class="anniversary-mark" role="img" aria-label="Faint anniversary emblem: outlined numerals 25 with the words For Over and a hand-lettered Years" viewBox="0 0 270 250">
      <defs>
        <linearGradient id="markTone" x1="0" y1="0" x2="1" y2="1">
          <stop offset="0" stop-color="#ec1f27" stop-opacity="0.05"/>
          <stop offset="1" stop-color="#3c3c3c" stop-opacity="0.05"/>
        </linearGradient>
      </defs>
      <rect width="270" height="250" rx="30" fill="url(#markTone)"/>
    </svg>
  </main>
</body>
</html>
```